Full revamp of cheap website design - the best designer will be offered a much larger project!

Corwell Tane are a progressive and innovative mid-tier professional services group (accountants and business advisors) with offices based in major cities throughout Australia and New Zealand.
Our positioning statement is "Energetic, Innovative, Streetwise", and the visual appearance must reflect this. Although still a relatively conservative industry, we aim to project a modern, innovative, energetic, highly professional but approachable image. The presentation should tie in with the theme "we take our work seriously, not ourselves".
Our aim with this new design is the elevate the status of the group in its online presentation and communication... we want to 'impress' and stand out from the crowd! See our existing site at www.corwelltane.com.au
We're looking for a special designer to take on the Web Site Design Concept - Uncoded - graphics only in line with the concept architecture we will provide (although we are flexible with the layout - we want an interface design that works!). Must work within the constraints of a suitable wordpress theme... Designer to source (we quite like thembrova.com as an option, but havn't seen any really slick representations of it)... there are many other great themes to choose from). Must include a series of slick flash banner designs.
or alternatively,
Design and coding (custom design theme) using wordpress platform (unless you can convince us of the benefits of using some other recognised and supported platform).
Happy to receive the design concepts as graphics only (but the flash is an important factor). You'll need to prove that it will work within an existing theme (or that you are capable of quickly developing a bug-free custom site on the wordpress platform.
Only highly talented and professional designers need enter, but the right designer will be well rewarded with the offer of a much larger design project and plenty of ongoing work.
Task
We are completely overhauling our existing and outdated website(s) x 9 and are looking for a new visual design concept (homepage plus one inside section homepage, one information page and one state homepage to start).
Once our executive have selected and approved the winning concept, we will offer you the opportunity to complete all other sections of the site including a variety of flash banners and other visual section headings, advertising and promotional pieces not only for the central corwelltane.com.au site, but for all of the state sites (8), which will replicate the central site with mainly banner and advertising changes. We will look after content entry.
This project will grow into quite a large opportunity for the right designer with ongoing design elements in the form of flash banners, banner ads, newsletter and other emarketing designs, plus related blogs and product sites required over time.
We will provide you with a flexible wireframe architecture from which to work, along with conceptual content and imagery where available (feel free to use stock images wherever necessary). If you need something else, just ask!
Deadline
Unfortunately, we need you to work to a ridiculously tight deadline on the concept design, due to a pending executive meeting (where we are committed to making a decision on the approved concept). We need your designs to be submitted by 3/11/2009. The good news is that we can get started on the full project reasonably quickly following the first deadline.
Some of our competitors:
www.lindqvistmoray.com.au
www.quillan.com.au
www.tessaly.com.au
www.zvr.com.au
www.gae.com.au
www.edgarmolloy.com.au
www.vantro.com.au
www.pellinggroup.com.au
www.tzr.com.au
www.glund.com
You'll need to contact me at renatao@corwelltane.net so that I can give you access to the resources you'll need to get the conceptual design job done. Just send me a quick note letting me know that you're interested in the contest.
Updates
Hello to all Corwell Tane website redesign competitors!
A quick hello to all our competitors!
Thank you for submitting your fabulous designs... I will be looking at each of them tomorrow (PM) and will provide you with individual feedback and in some cases, requests for minor modifications prior to our Executive presentation on the 6th. Once again, I do apologise for the delay in my response and the rush required at your end.
Many thanks
Renata
Hello,
I have extended the deadline via ArtQuarry to enable you to make the requested changes and get them back to me asap TODAY!
Although I only extended the deadline by 1 day, it is now showing as almost 2 days left. This is not the case. I MUST have your revised designs as soon as possible TODAY.
Many thanks for your great work!
Renata
Hi!
Hello Art Quarry Contestants!
I'm terribly sorry about the delay... still waiting on the OK from our Senior Executive members on which design we will pursue. I am chasing an answer and will get back to you as soon as possible.
Many thanks for your patience.
Renata
Target Market(s)
Our primary target is the mid-size SME marketplace with turnover $5 - $50mil (CFO, COO, MD, GM - ie, Senior Executives) plus High Net worth individuals and high quality staff.
Corwell Tane's target market are clients who have (and are) invested in their businesses and/or themselves but now need our assistance to grow and develop further.
They need accountants and advisers who can deliver more than the fundamentals. Our clients are defined by an attitude that motivates them to seek out opportunities while putting the structures in place to ensure the security of their futures.
Number of Pages Required
4 pages
Requirements
Must have
- Designs must be clean and uncluttered whilst maintaining a slick and professional yet approachable look and feel.
The corporate logo must be used and unchanged.
A series of attractive, text based flash animated banners will be required to highlight our key messaging
All of the page components as outlined in the concept design provided are required (although layout and other suggested modifications are welcomed).
As noted earlier, you need to contact me at renatao@corwelltane.net so that I can give you access to the resources you''ll need to get the conceptual design job done. Just send me a quick note letting me know that you''re interested in the content.
Nice to have
- If possible (although not absolutely necessary), consideration should be made regarding tying in our NZ member firm''s site design at www.corwelltane.co.nz (which will not change) along with www.veldrinalliance.com. Although we don''t wish to replicate either of these designs, it would be nice to somehow connect them visually in some way. Certainly the site map at the bottom of the page (like the NZ site) must be maintained.
If you want to chat through the brief you are welcome to call or IM me on skype: renata.oblomova
Should not have
- images of abacus''s!

```html
<!DOCTYPE html>
<html lang="en">
<head>
<meta charset="utf-8">
<title>Corwell Tane – Accountants &amp; Business Advisers</title>
<link rel="stylesheet" href="https://fonts.googleapis.com/css2?family=Roboto+Condensed:wght@400;700&family=Open+Sans:wght@400;600&display=swap">
<style>
:root{
  --bar:#3a3a3a;
  --sky-top:#3e6a8c;
  --sky-mid:#6f95b2;
  --sky-low:#9db6c9;
  --suits:#2b2f36;
  --white:#ffffff;
  --panel:#f1f1f1;
  --panel-edge:#e2e2e2;
  --rule:#c9c9c9;
  --nav-text:#3b3b3b;
  --nav-active:#cfd6dc;
  --nav-num:#ffffff;
  --heading:#3f6584;
  --body:#8a8a8a;
  --link:#4a6f8f;
  --foot-text:#c9c9c9;
}
*{box-sizing:border-box;margin:0;padding:0}
html,body{width:1149px;height:1200px;overflow:hidden;background:var(--white)}
body{position:relative;font-family:"Open Sans",Tahoma,sans-serif;color:var(--body)}
.abs{position:absolute}

/* top bar */
.topbar{left:0;top:0;width:1149px;height:54px;background:var(--bar)}
.topbar .label{font-family:"Roboto Condensed",sans-serif;font-weight:700;color:#b9c2ca;font-size:18px;top:14px}
.firm-select{left:178px;top:12px;width:194px;height:26px;background:var(--white);border-radius:4px;border:1px solid #888;font-size:16px;color:#222;padding:2px 8px}
.firm-select .arrow{position:absolute;right:2px;top:2px;width:22px;height:20px;background:#3f76c4;border-radius:3px}
.go-btn{left:380px;top:9px;width:47px;height:32px;border-radius:5px;background:linear-gradient(#ffffff,#d5dde6);border:1px solid #9aa7b4;color:#2e6cb4;font-weight:700;font-size:17px;text-align:center;line-height:30px}
.search-box{left:873px;top:12px;width:252px;height:27px;background:var(--white);border:1px solid #999}

/* hero */
.hero{left:0;top:54px;width:1149px;height:326px;background:linear-gradient(180deg,var(--sky-top) 0%,var(--sky-mid) 55%,var(--sky-low) 100%)}
.hero-people{left:750px;top:54px;width:399px;height:326px;background:linear-gradient(90deg,rgba(43,47,54,0) 0%,var(--suits) 25%,#3a3f48 60%,var(--suits) 100%)}
.hero-rule{left:0;top:380px;width:1149px;height:4px;background:var(--bar)}
.brand-box{left:33px;top:177px;width:354px;height:125px;background:var(--white);display:flex;align-items:center;gap:16px;padding-left:28px}
.brand-box .mark{width:26px;height:26px;background:var(--heading)}
.brand-box .name{font-weight:600;font-size:32px;color:#4a4a4a}
.promo{left:423px;top:177px;width:359px;height:201px;background:rgba(215,228,238,.35);border:1px solid rgba(255,255,255,.3)}
.promo h2{position:absolute;left:36px;top:16px;font-family:"Roboto Condensed",sans-serif;font-weight:700;font-size:30px;line-height:30px;color:var(--white);letter-spacing:-.5px}
.promo h3{position:absolute;left:36px;top:44px;font-family:"Roboto Condensed",sans-serif;font-weight:700;font-size:22px;color:#e6eef4}
.promo ul{position:absolute;left:24px;top:85px;list-style:none}
.promo li{font-size:15px;line-height:21px;color:var(--white);text-decoration:underline}
.promo li::before{content:"•";display:inline-block;width:16px}
.promo .more{position:absolute;left:157px;top:165px;font-family:"Roboto Condensed",sans-serif;font-weight:700;font-size:17px;color:var(--white)}

/* nav */
.nav-panel{left:33px;top:324px;width:355px;height:383px;background:var(--panel);border-right:2px solid var(--panel-edge)}
.nav-item{position:absolute;left:40px;width:206px;font-family:"Roboto Condensed",sans-serif;font-size:24px;color:var(--nav-text);padding-left:15px}
.nav-item.active{background:var(--nav-active);height:47px;line-height:47px;top:28px;padding-right:14px;display:flex;justify-content:space-between;color:#4b4b4b}
.nav-item.active .num{color:var(--nav-num)}
.nav-rule{position:absolute;left:40px;width:206px;height:1px;background:var(--rule)}

/* in the know */
.know{left:33px;top:733px;width:355px;height:200px;background:#e7e7e7}
.know h2{position:absolute;left:29px;top:10px;font-family:"Roboto Condensed",sans-serif;font-size:27px;color:var(--heading)}
.know .k-rule{position:absolute;left:20px;top:48px;width:318px;height:1px;background:#b8b8b8}
.know h3{position:absolute;left:24px;top:55px;font-size:19px;font-weight:600;color:#6e6e6e}
.know .sub{position:absolute;left:24px;top:80px;font-size:14px;color:#7a7a7a}
.know p{position:absolute;left:24px;top:108px;width:318px;font-size:14px;line-height:17px;color:#8a8a8a}

/* articles */
.thumb{width:192px;height:141px;background:linear-gradient(135deg,#cfe0ea 0%,#8fa9bb 45%,#2d2f35 100%);box-shadow:2px 3px 6px rgba(0,0,0,.25);border:4px solid var(--white)}
.article h2{position:absolute;left:669px;font-family:"Roboto Condensed",sans-serif;font-weight:400;font-size:27px;line-height:31px;color:var(--heading);width:420px}
.article p{position:absolute;left:669px;width:450px;font-size:15px;line-height:21px;color:var(--body)}
.article a{position:absolute;right:62px;font-size:15px;color:var(--link);text-decoration:underline}
.divider{left:426px;top:588px;width:687px;height:1px;background:#d4d4d4}

/* footer */
.footer{left:0;top:975px;width:1149px;height:225px;background:var(--bar);color:var(--foot-text);font-size:15px}
.footer span{position:absolute}
</style>
</head>
<body>

<div class="abs topbar">
  <span class="abs label" style="left:60px">Member Firms:</span>
  <div class="abs firm-select">Adelaide<span class="arrow"></span></div>
  <div class="abs go-btn">Go</div>
  <span class="abs label" style="left:807px">SEARCH</span>
  <div class="abs search-box"></div>
</div>

<div class="abs hero"></div>
<div class="abs hero-people" role="img" aria-label="Photo of three smiling business people in dark suits"></div>
<div class="abs hero-rule"></div>

<div class="abs brand-box"><span class="mark"></span><span class="name">Corwell Tane</span></div>

<div class="abs promo">
  <h2>WHERE TO NEXT?</h2>
  <h3>business solutions</h3>
  <ul>
    <li>Sed ut perspiciatis unde</li>
    <li>Omnis iste natuerror voluptatem</li>
    <li>Accus doloremque</li>
  </ul>
  <span class="more">» know more</span>
</div>

<nav class="abs nav-panel">
  <div class="nav-item active"><span class="num">01.</span><span>ABOUT</span></div>
  <div class="nav-item" style="top:96px">SERVICES</div>
  <div class="nav-rule" style="top:136px"></div>
  <div class="nav-item" style="top:152px">OUR NETWORK</div>
  <div class="nav-rule" style="top:194px"></div>
  <div class="nav-item" style="top:214px">INSIGHTS</div>
  <div class="nav-rule" style="top:256px"></div>
  <div class="nav-item" style="top:282px">CONTACT</div>
  <div class="nav-rule" style="top:316px"></div>
  <div class="nav-item" style="top:334px">LOGIN</div>
</nav>

<aside class="abs know">
  <h2>In the Know...</h2>
  <div class="k-rule"></div>
  <h3>An idea to save you thousands!</h3>
  <span class="sub">Business Briefings</span>
  <p>The Central Reserve Board has removed almost all of the mystery about what is going to happen with interest rates. Rates have bottomed out and are likely to start going up. more&gt;&gt;&gt;</p>
</aside>

<div class="abs thumb" style="left:433px;top:417px" role="img" aria-label="Photo of three smiling colleagues"></div>
<div class="article">
  <h2 style="top:411px">The threat to businesses with<br>unrelated shareholders</h2>
  <p style="top:477px">Sed ut perspiciatis unde omnis iste natus error sit voluptatem accusantium doloremque laudantium, totam rem aperiam,</p>
  <a style="top:542px">Click here to find out more &gt;&gt;&gt;</a>
</div>
<div class="abs divider"></div>

<div class="abs thumb" style="left:433px;top:610px" role="img" aria-label="Photo of three smiling colleagues"></div>
<div class="article">
  <h2 style="top:606px">Is good cash flow management<br>enough to save your business?</h2>
  <p style="top:672px">Sed ut perspiciatis unde omnis iste natus error sit voluptatem accusantium doloremque laudantium, totam rem aperiam,</p>
  <a style="top:737px">Click here to find out more &gt;&gt;&gt;</a>
</div>

<div class="abs thumb" style="left:433px;top:794px" role="img" aria-label="Photo of three smiling colleagues"></div>
<div class="article">
  <h2 style="top:792px">Are you ready for Private Equity?</h2>
  <p style="top:852px">Sed ut perspiciatis unde omnis iste natus error sit voluptatem accusantium doloremque laudantium, totam rem aperiam,</p>
  <a style="top:905px">Click here to find out more &gt;&gt;&gt;</a>
</div>

<footer class="abs footer">
  <span style="left:48px;top:14px">About</span>
  <span style="left:372px;top:14px">Services</span>
  <span style="left:547px;top:14px">Network</span>
  <span style="left:729px;top:14px">Knowledge</span>
  <span style="left:66px;top:50px">* Innovative, Energetic, Streetsmart</span>
  <span style="left:66px;top:68px">* Leadership team</span>
  <span style="left:51px;top:122px">Etc</span>
  <span style="left:57px;top:191px">© 2006 Business Company &nbsp;|&nbsp; Privacy Policy</span>
</footer>

</body>
</html>
```